HollowPine Ventures Inc. Business Card Design

My business is custom renovations and homes.I would need to have a new business logo created to go along with my company name. The business card should be of a modern style as this is the market I am focused on. I would need my contact information and website posted on the card. I would also like to list a few of the tasks I conduct on the card (such as: Renovations, Additions, Repairs, New Homes, Design, Consultations). On the reverse of the card I currently have just my logo and my motto, "Shaping A Bold Path". However, I am open to completely changing everything as I am starting a new year and would like to excel further. Any new ideas and suggestions are always welcomed. Thank you.

Target Market(s)

Upscale residential and commercial renovations and builds

Industry/Entity Type

Business

Contact Information for Business Card

I would like the design to be able to be laser cut or burnt onto a wooden business card. I will be creating one option of cards for really loyal customers (wooden) and a second option for the everyday customer (paper).

Font styles to use
Other font styles liked:
• Calibri / anything of mordern taste

Colors
f37122
5c5c5c
474747
ffffff

Requirements
Must have
• I would like the colours of my business to be a sharp orange and grey. I believe this will symbolize a modern style. I am open to other suggestions if this is not suitable for the designers tastes. My contact info as follows:
• Will Marsh
• President
• HollowPine Ventures Inc.
• 555-214-3987
• will@hollowpineventures.example
• I would like my website (currently under construction) hollowpineventures.example on the card aswell.
Nice to have
• Along with a modern logo representing HollowPine, I would like something on the card besides the logo and contact information. Perhaps a small background design. I feel it may be nice to have my services listed on the card (in smaller font on the bottom) Renovations, Additions, Repairs, Design, Consultations.
Should not have
• The business card should not have too many different colors. Should not have rounded corners.

```html
<!DOCTYPE html>
<html lang="en">
<head>
<meta charset="utf-8">
<title>HollowPine Ventures Inc. — Business Card</title>
<link rel="stylesheet" href="https://fonts.googleapis.com/css2?family=Open+Sans:wght@400;600;700&display=swap">
<style>
  :root {
    --orange: #f37122;
    --grey: #5c5c5c;
    --grey-dark: #474747;
    --white: #ffffff;
    --backdrop: #ecebe8;
  }
  * { margin: 0; padding: 0; box-sizing: border-box; }
  html, body { width: 1200px; height: 900px; overflow: hidden; }
  body {
    background: var(--backdrop);
    font-family: "Open Sans", Arial, sans-serif;
    position: relative;
  }
  .card {
    position: absolute;
    left: 250px;
    width: 700px;
    height: 400px;
    overflow: hidden;
    box-shadow: 0 6px 18px rgba(0,0,0,0.18);
  }

  /* Reverse side */
  .card-back {
    top: 30px;
    background: var(--orange);
    color: var(--white);
    display: flex;
    flex-direction: column;
    align-items: center;
    justify-content: center;
  }
  .brand-mark {
    display: flex;
    align-items: center;
    gap: 16px;
  }
  .brand-mark .square {
    width: 34px; height: 34px;
    background: currentColor;
  }
  .card-back .brand-name {
    font-size: 52px;
    font-weight: 600;
    letter-spacing: 1px;
  }
  .motto {
    margin-top: 26px;
    font-size: 27px;
    font-weight: 400;
    letter-spacing: 1px;
    text-transform: uppercase;
  }

  /* Front side */
  .card-front {
    top: 470px;
    background: var(--white);
    color: var(--grey-dark);
  }
  .corner-mark { position: absolute; left: 0; top: 0; }
  .holder { position: absolute; left: 78px; top: 26px; line-height: 1.1; }
  .holder-name { color: var(--orange); font-weight: 700; font-size: 19px; }
  .holder-title { color: var(--grey-dark); font-size: 15px; }

  .card-front .brand-mark {
    position: absolute;
    left: 300px;
    top: 118px;
    color: var(--orange);
    gap: 12px;
  }
  .card-front .brand-mark .square { width: 26px; height: 26px; }
  .card-front .brand-name { font-size: 30px; font-weight: 600; }

  .contact-list {
    position: absolute;
    left: 48px;
    top: 178px;
    list-style: none;
    font-size: 16px;
    line-height: 25px;
  }
  .contact-list li { display: flex; align-items: center; gap: 10px; }
  .contact-list svg { width: 13px; height: 13px; fill: var(--orange); flex: none; }

  .services {
    position: absolute;
    left: 48px;
    top: 268px;
    font-size: 19px;
    color: var(--grey-dark);
    word-spacing: 1px;
  }
  .bands { position: absolute; left: 0; bottom: 0; }
</style>
</head>
<body>

  <section class="card card-back">
    <div class="brand-mark">
      <span class="square"></span>
      <span class="brand-name">HollowPine</span>
    </div>
    <p class="motto">Shaping A Bold Path</p>
  </section>

  <section class="card card-front">
    <svg class="corner-mark" width="70" height="60" viewBox="0 0 70 60">
      <polygon points="0,0 14,0 0,14" fill="var(--orange)"/>
      <polygon points="22,0 60,0 60,52 0,52 0,36" fill="var(--grey)"/>
    </svg>
    <div class="holder">
      <p class="holder-name">Will Marsh</p>
      <p class="holder-title">President</p>
    </div>

    <div class="brand-mark">
      <span class="square"></span>
      <span class="brand-name">HollowPine Ventures Inc.</span>
    </div>

    <ul class="contact-list">
      <li>
        <svg viewBox="0 0 24 24"><path d="M6.6 10.8a15.1 15.1 0 0 0 6.6 6.6l2.2-2.2a1 1 0 0 1 1-.25 11.4 11.4 0 0 0 3.6.57 1 1 0 0 1 1 1V20a1 1 0 0 1-1 1A17 17 0 0 1 3 4a1 1 0 0 1 1-1h3.5a1 1 0 0 1 1 1c0 1.25.2 2.45.57 3.57a1 1 0 0 1-.25 1z"/></svg>
        555-214-3987
      </li>
      <li>
        <svg viewBox="0 0 24 24"><path d="M2 5h20v14H2z M2 5l10 8 10-8" stroke="var(--white)" stroke-width="1.5"/></svg>
        will@hollowpineventures.example
      </li>
      <li>
        <svg viewBox="0 0 24 24"><circle cx="12" cy="12" r="11"/><path d="M1 12h22M12 1c4 4 4 18 0 22M12 1c-4 4-4 18 0 22" stroke="var(--white)" stroke-width="1.5" fill="none"/></svg>
        www.hollowpineventures.example
      </li>
    </ul>

    <p class="services">Renovations | Additions | Repairs | New Homes | Design | Consultations</p>

    <svg class="bands" width="700" height="90" viewBox="0 0 700 90">
      <polygon points="0,24 290,24 272,48 0,48" fill="var(--orange)"/>
      <polygon points="290,48 700,48 700,90 258,90" fill="var(--grey)"/>
    </svg>
  </section>

</body>
</html>
```